Business Card Design Project

We need a business card for our new business based in Vancouver called
"Lumora Calm House" We are looking for a simple yet bold design for our business cards that will enable us to stand out from the pack. All business card details will be provided in the handover stage.
Updates

Thank you to all who have submitted

The work is great for the most part
Cards with creative use of the logo
have been more successful so far

Dark cards and rounded edges 
are also getting good reviews

Double sided is an option we would like to see explored

Thank you

Target Market(s)

Our clients are stressed business people, yoga/meditation enthusiast, and people looking for a new experience in a Spa enviroment

Industry/Entity Type

Business

Font styles to use
Other font styles liked:
• please check design file

Requirements
Must have
• Lumora Calm House

5218 E Kestrel Row, Vancouver, BC V5N 4K7

lumora@calmhaven.ca
Nice to have
• Creative approach to layout and design

Outside of the box design elements
Should not have
• Should not be too busy

```html
<!DOCTYPE html>
<html lang="en">
<head>
<meta charset="utf-8">
<title>Lumora Calm House — Business Card</title>
<link rel="stylesheet" href="https://fonts.googleapis.com/css2?family=Open+Sans:wght@300;400&display=swap">
<style>
  :root {
    --backdrop: #c6e8de;
    --card-navy: #0a0c2b;
    --accent-orange: #e9811f;
  }
  * { margin: 0; padding: 0; box-sizing: border-box; }
  html, body {
    width: 1200px;
    height: 900px;
    overflow: hidden;
    background: var(--backdrop);
    font-family: "Open Sans", Arial, sans-serif;
  }
  .canvas {
    width: 1200px;
    height: 900px;
    display: flex;
    align-items: center;
    justify-content: center;
  }
  .business-card {
    width: 700px;
    height: 400px;
    background: var(--card-navy);
    border-radius: 34px;
    position: relative;
    color: var(--accent-orange);
  }
  .brand {
    position: absolute;
    top: 92px;
    left: 0;
    right: 0;
    display: flex;
    align-items: center;
    justify-content: center;
    gap: 18px;
  }
  .brand-dot {
    width: 40px;
    height: 40px;
    border-radius: 50%;
    background: var(--accent-orange);
    flex: none;
  }
  .brand-name {
    font-size: 42px;
    font-weight: 300;
    letter-spacing: 1px;
    white-space: nowrap;
  }
  .contact {
    position: absolute;
    left: 0;
    right: 0;
    top: 222px;
    text-align: center;
    font-size: 16px;
    font-style: normal;
    line-height: 1;
  }
  .contact-address { margin-bottom: 28px; }
</style>
</head>
<body>
  <main class="canvas">
    <section class="business-card">
      <div class="brand">
        <span class="brand-dot" aria-hidden="true"></span>
        <h1 class="brand-name">Lumora Calm House</h1>
      </div>
      <address class="contact">
        <p class="contact-address">5218 E Kestrel Row, Vancouver, BC V5N 4K7</p>
        <p class="contact-email">lumora@calmhaven.ca</p>
      </address>
    </section>
  </main>
</body>
</html>
```